Plakat Ausbildung für Handwerksbetrieb
Zielgruppe
Wir sind ein Handwerksbetrieb und möchten mit einem Banner auf unsere Ausbildungsplätze hinweisen und junge Menschen (vor allem Schüler + Studenten) ansprechen. Der Banner soll nach Möglichkeit quadratisch sein. Unser bisheriges Logo habe ich als Datei angehängt. Desweiteren ein Bild wie ich es mir in etwa vorstellen würde das sich die 3 Elemente (Feuer, Wasser und Strom als Synonym für Heizung, Sanitär und Elektro) darstellen. Dazu noch eine knappe Beschreibung welche Ausbildungsplätze wir anbieten und auf unsere Homepage verweisen.
Aufgabenstellung
Ausbildungsplätze als:
- Anlagenmechaniker/in für Sanitär-, Heizungs- und Klimatechnik
- Elektroinstallateur/in (Energie- und Gebäudetechnik)

```html
<!DOCTYPE html>
<html lang="de">
<head>
<meta charset="utf-8">
<title>Ausbildungsplätze – Plakat</title>
<link rel="stylesheet" href="https://fonts.googleapis.com/css2?family=Anton&family=Montserrat:wght@700&display=swap">
<style>
  :root {
    --black: #000000;
    --white: #ffffff;
    --yellow: #fcc71c;
    --red: #e41e26;
    --blue: #0a63b4;
  }
  html, body {
    margin: 0;
    padding: 0;
    width: 1200px;
    height: 1200px;
    overflow: hidden;
    background: var(--black);
  }
  .poster {
    position: relative;
    width: 1200px;
    height: 1200px;
    background: var(--black);
    overflow: hidden;
    font-family: "Montserrat", Arial, sans-serif;
  }
  .hero-visual {
    position: absolute;
    left: 0;
    top: 330px;
    width: 1200px;
    height: 835px;
    background:
      radial-gradient(ellipse 38% 45% at 88% 65%, rgba(245,120,30,0.9), rgba(140,40,10,0.5) 55%, transparent 80%),
      radial-gradient(ellipse 30% 40% at 12% 78%, rgba(40,60,200,0.75), transparent 75%),
      radial-gradient(ellipse 35% 30% at 55% 55%, rgba(70,20,10,0.7), transparent 80%),
      linear-gradient(180deg, var(--black) 0%, #120806 35%, #1a0b07 100%);
  }
  .brand {
    position: absolute;
    left: 107px;
    top: 93px;
    height: 67px;
    display: flex;
    align-items: center;
    gap: 9px;
  }
  .brand-mark {
    width: 66px;
    height: 66px;
    background: var(--white);
  }
  .brand-name {
    font-family: "Montserrat", Arial, sans-serif;
    font-weight: 700;
    font-size: 24px;
    color: var(--white);
    letter-spacing: 1px;
    white-space: nowrap;
  }
  .headline {
    position: absolute;
    margin: 0;
    font-family: "Anton", Impact, sans-serif;
    font-weight: 400;
    text-transform: uppercase;
    line-height: 1;
    white-space: nowrap;
  }
  .headline--top {
    right: 110px;
    top: 92px;
    font-size: 100px;
    color: var(--white);
    letter-spacing: 1px;
  }
  .headline--bottom {
    right: 108px;
    top: 210px;
    font-size: 102px;
    color: var(--yellow);
  }
  .offer-box {
    position: absolute;
    left: 179px;
    top: 391px;
    width: 842px;
    height: 227px;
    box-sizing: border-box;
    border: 5px solid #f2f2f2;
    border-radius: 20px;
    background: linear-gradient(180deg, rgba(0,0,0,0.95), rgba(0,0,0,0.6));
  }
  .trade-icon {
    position: absolute;
    top: 327px;
    width: 142px;
    height: 142px;
  }
  .trade-icon--plumbing { left: 354px; }
  .trade-icon--electric { left: 743px; }
  .trade-title {
    position: absolute;
    top: 480px;
    width: 400px;
    margin: 0;
    text-align: center;
    color: var(--white);
    font-weight: 700;
    font-size: 25px;
    line-height: 32px;
  }
  .trade-title--plumbing { left: 225px; }
  .trade-title--electric { left: 614px; }
  .accent-bands {
    position: absolute;
    left: 0;
    bottom: 0;
    width: 1200px;
    height: 35px;
  }
</style>
</head>
<body>
<main class="poster">
  <div class="hero-visual" role="img" aria-label="Eishockeypuck umgeben von Wasserspritzern, Blitzen und Flammen als Sinnbild für Sanitär, Elektro und Heizung"></div>

  <div class="brand">
    <div class="brand-mark"></div>
    <span class="brand-name">NORDHAVEN</span>
  </div>

  <h1 class="headline headline--top">Wir bieten einen</h1>
  <p class="headline headline--bottom">Ausbildungsplätze als</p>

  <div class="offer-box"></div>

  <svg class="trade-icon trade-icon--plumbing" viewBox="0 0 142 142" aria-hidden="true">
    <circle cx="71" cy="71" r="66" fill="#0b0b0b" stroke="var(--red)" stroke-width="6"/>
    <g fill="none" stroke="#ffffff" stroke-width="11" stroke-linecap="round">
      <line x1="44" y1="44" x2="98" y2="98"/>
      <line x1="98" y1="44" x2="44" y2="98"/>
    </g>
    <circle cx="44" cy="44" r="11" fill="#ffffff"/>
    <circle cx="98" cy="98" r="13" fill="none" stroke="#ffffff" stroke-width="7"/>
    <circle cx="98" cy="44" r="13" fill="none" stroke="#ffffff" stroke-width="7"/>
    <circle cx="44" cy="98" r="13" fill="none" stroke="#ffffff" stroke-width="7"/>
  </svg>

  <svg class="trade-icon trade-icon--electric" viewBox="0 0 142 142" aria-hidden="true">
    <circle cx="71" cy="71" r="66" fill="#0b0b0b" stroke="var(--blue)" stroke-width="6"/>
    <polygon points="78,28 44,78 68,78 58,114 98,58 73,58 90,28" fill="#ffffff"/>
  </svg>

  <p class="trade-title trade-title--plumbing">Anlagenmechaniker/in<br>für Sanitär-, Heizungs- und<br>Klimatechnik</p>
  <p class="trade-title trade-title--electric">Elektroinstallateur/in<br>(Energie- und<br>Gebäudetechnik)</p>

  <svg class="accent-bands" viewBox="0 0 1200 35" aria-hidden="true">
    <polygon points="0,0 598,0 580,35 0,35" fill="var(--blue)"/>
    <polygon points="618,0 1200,0 1200,35 600,35" fill="var(--red)"/>
  </svg>
</main>
</body>
</html>
```